Client website

Our designer we were working with had some personal things come up and was unable to finish the design for the site.

We have a .psd file started, and will be attaching it to the project.
Updates

Reason: I still want to polish the designs with the current designer and allow more designers the opportunity to participate.

Reason: I'm extending the deadline for another day to give everyone enough time for the final changes our client wants.

I'm trying to extend the deadline so we can get one last set of comps in for my client.  Could everyone message me and let me know how much time they need to do the final tweaks?

Reason: Hey everyone.  I've been sick the last 3 days and I haven't been able to provide feedback on designs.  I'm extending just a few more days so I can catch up here.  Thanks everyone for your patience.

Target Market(s)

Adults in United States aged 25 to 60 that handle the household budgets and maintenance.

Requirements
Must have
• 1) We need 2 pages. 1 page for flood restoration, 1 page for carpet cleaning

2) The 1-800-# must be the focal point of the website for both pages. People are mostly looking to contact someone ASAP to get them out to their house when flooding occurs.

3) We''re going to have a slide show area to high-light different sub-services offered for each page.

4) We really want a frendloop / quipsy feed area. We''re going to use frendloop for special offers, and quipsy for weather updates. The frendloop feed is going to be on the carpet cleaning page. The quipsy feed is going to be on the flood page.

5) We want an SEO text sections near the bottom.

6) The very bottom will link to the privacy policy and user agreement as well as company name and copyright details.

We really want to stick to the say "theme" that our first designer started with.
Nice to have
• I'm not a designer, so if you think something looks better somewhere, or something can be eliminated, or something can be enhanced, but all means, let us know.

```html
<!DOCTYPE html>
<html lang="en">
<head>
<meta charset="utf-8">
<title>Clearwell – Water &amp; Fire Damage Restoration</title>
<link rel="stylesheet" href="https://fonts.googleapis.com/css2?family=Arimo:wght@400;700&family=Open+Sans:wght@400;600;700&display=swap">
<style>
:root{
  --page-bg:#1b3244;
  --navy:#0d2c4a;
  --accent:#2a7fc4;
  --nav-top:#0a5a9c;
  --nav-bottom:#063f73;
  --nav-active:#8fd0ff;
  --sea-top:#2a8fcf;
  --sea-bottom:#2a9fdc;
  --panel:rgba(120,190,235,0.28);
  --panel-line:rgba(255,255,255,0.25);
  --link:#bfe6ff;
  --white:#ffffff;
}
*{margin:0;padding:0;box-sizing:border-box}
html,body{width:1200px;height:960px;overflow:hidden}
body{background:var(--page-bg);font-family:"Open Sans",Tahoma,sans-serif;color:var(--white);position:relative}
.site{position:absolute;left:113px;top:33px;width:975px;height:859px;border-radius:10px;overflow:hidden;
  background:linear-gradient(180deg,var(--sea-top) 0%,#2f96d4 50%,var(--sea-bottom) 100%)}
.header{position:absolute;left:0;top:0;width:975px;height:320px}
.header-art{position:absolute;inset:0;background:linear-gradient(100deg,#ffffff 0%,#eef6fc 35%,#d7ebf8 70%,#bcdcf1 100%)}
.brand{position:absolute;left:50px;top:220px;display:flex;align-items:center;gap:14px}
.brand-dot{width:44px;height:44px;border-radius:50%;background:var(--accent);flex:none}
.brand-text{display:flex;flex-direction:column}
.brand-name{font-family:"Open Sans",Tahoma,sans-serif;font-weight:600;font-size:40px;line-height:46px;color:var(--navy);white-space:nowrap}
.brand-tagline{font-family:"Open Sans",Tahoma,sans-serif;font-weight:600;font-size:14px;line-height:20px;color:var(--navy);white-space:nowrap}
.call-box{position:absolute;left:623px;top:18px;width:335px;height:91px;border-radius:10px;
  background:linear-gradient(180deg,#ffffff,#e4eef5);box-shadow:0 2px 8px rgba(0,40,80,.25);border:1px solid #ffffff}
.call-label{position:absolute;left:21px;top:13px;font-family:Arimo,Arial,sans-serif;font-weight:700;font-size:24px;color:var(--navy)}
.call-number{position:absolute;left:17px;top:33px;font-family:Arimo,Arial,sans-serif;font-weight:700;font-size:42px;line-height:48px;color:var(--navy);letter-spacing:-0.3px;white-space:nowrap}
.nav{position:absolute;left:0;top:320px;width:975px;height:46px;background:linear-gradient(180deg,var(--nav-top),var(--nav-bottom));
  display:flex;align-items:center;padding-left:54px}
.nav a{font-family:"Open Sans",sans-serif;font-weight:600;font-size:16px;color:var(--white);text-decoration:none;padding:0 22px;border-left:1px solid rgba(255,255,255,.6);line-height:12px}
.nav a:first-child{border-left:none;padding-left:0;color:var(--nav-active)}
.sea-band{position:absolute;left:0;top:366px;width:975px;height:60px;background:linear-gradient(180deg,#5fb4e2,rgba(47,150,212,0))}
.feed{position:absolute;top:431px;width:463px;height:270px;background:var(--panel);border:1px solid var(--panel-line);border-radius:5px}
.feed--frendloop{left:20px}
.feed--quipsy{left:493px}
.feed-badge{position:absolute;top:-50px;left:22px;width:70px;height:70px;border-radius:8px;background:linear-gradient(160deg,#3d6fb5,#1b3d7a);box-shadow:0 3px 6px rgba(0,0,0,.3)}
.feed--quipsy .feed-badge{background:linear-gradient(160deg,#7fd0f5,#2a8fd0)}
.feed-title{position:absolute;top:-34px;left:147px;font-family:Arimo,Arial,sans-serif;font-weight:700;font-size:24px;color:var(--white);white-space:nowrap;text-shadow:0 1px 2px rgba(0,40,80,.4)}
.feed--quipsy .feed-title{left:122px}
.posts{position:absolute;left:10px;top:49px;width:446px;list-style:none}
.post{font-size:10.5px;line-height:14px;letter-spacing:-0.15px}
.post:nth-child(1){margin-bottom:16px}
.post:nth-child(2){margin-bottom:10px}
.post-meta{display:flex;align-items:center;height:20px;margin-top:8px;font-weight:700;font-size:11px;letter-spacing:0;white-space:nowrap}
.post-meta .user{color:var(--link);margin-left:4px}
.post-meta .sep{margin:0 9px;opacity:.8;font-weight:400}
.action-btn{display:inline-block;height:20px;line-height:18px;padding:0 7px;border:1px solid #c8d4e4;border-radius:3px;background:linear-gradient(#ffffff,#e6ecf3);color:#3b5b8a;font-weight:600;font-size:11px}
.count{display:inline-block;margin-left:6px;height:20px;line-height:18px;width:34px;text-align:center;border:1px solid #c8d4e4;border-radius:3px;background:#fff;color:#333;font-size:11px}
.footer-nav{position:absolute;left:0;top:726px;width:975px;height:133px;background:linear-gradient(180deg,rgba(255,255,255,.06),rgba(40,170,225,.5));border-top:1px solid rgba(255,255,255,.2);display:flex}
.footer-col{position:relative;height:133px;border-right:1px solid rgba(0,60,120,.18)}
.footer-col:last-child{border-right:none}
.footer-col h3{height:29px;line-height:29px;padding-left:var(--pad);font-size:11px;font-weight:700;border-bottom:1px solid rgba(255,255,255,.2)}
.footer-col ul{list-style:none;padding:7px 0 0 var(--pad)}
.footer-col li{font-size:10.5px;line-height:18px;letter-spacing:-0.1px;position:relative;padding-left:11px;white-space:nowrap}
.footer-col li::before{content:"";position:absolute;left:1px;top:8px;width:2px;height:2px;background:rgba(255,255,255,.7)}
.copyright{position:absolute;top:919px;left:0;width:1200px;text-align:center;font-size:10px;color:#e8eef3}
</style>
</head>
<body>
<div class="site">
  <header class="header">
    <div class="header-art" role="img" aria-label="Light blue background with a flowing splash of clear water"></div>
    <div class="brand">
      <div class="brand-dot"></div>
      <div class="brand-text">
        <div class="brand-name">Clearwell</div>
        <div class="brand-tagline">Water &amp; Fire Damage Restoration</div>
      </div>
    </div>
    <div class="call-box">
      <div class="call-label">CALL US</div>
      <div class="call-number">1-800-555-0148</div>
    </div>
  </header>

  <nav class="nav">
    <a href="#">HOME</a><a href="#">ABOUT</a><a href="#">SERVICES</a><a href="#">FAQ</a><a href="#">CONTACT</a>
  </nav>
  <div class="sea-band" role="img" aria-label="Soft ocean horizon backdrop"></div>

  <section class="feed feed--frendloop">
    <div class="feed-badge"></div>
    <h2 class="feed-title">Find us on frendloop</h2>
    <ul class="posts">
      <li class="post">Lorem ipsum dolor sit amet, consectetur adipiscing elit. Sed quis ante felis. Donec porta arcu vehicula purus hendrerit interdum. Suspendisse lacus magna ullamcorper ut aliquet rutrum
        <div class="post-meta">Posted by: <span class="user">username details</span><span class="sep">|</span>2 hrs ago<span class="sep">|</span><span class="action-btn">Like</span></div></li>
      <li class="post">Curabitur laoreet, elit in tincidunt condimentum, massa tortor adipiscing nisl, non condimentum orci nunc quis diam. Curabitur sed arcu ut ipsum tempor molestie sed eget ipsum.
        <div class="post-meta">Posted by: <span class="user">username details</span><span class="sep">|</span>2 hrs ago<span class="sep">|</span><span class="action-btn">Like</span></div></li>
      <li class="post">Vivamus tempor feugiat felis nec fringilla. Aenean condimentum nunc ut felis pellentesque in aliquet orci pharetra. Duis pharetra pharetra est vel bibendum.
        <div class="post-meta">Posted by: <span class="user">username details</span><span class="sep">|</span>2 hrs ago<span class="sep">|</span><span class="action-btn">Like</span></div></li>
    </ul>
  </section>

  <section class="feed feed--quipsy">
    <div class="feed-badge"></div>
    <h2 class="feed-title">Follow us on quipsy</h2>
    <ul class="posts">
      <li class="post">Lorem ipsum dolor sit amet, consectetur adipiscing elit. Sed quis ante felis. Donec porta arcu vehicula purus hendrerit interdum. Suspendisse lacus magna ullamcorper ut aliquet rutrum
        <div class="post-meta">Posted by: <span class="user">username details</span><span class="sep">|</span>2 hrs ago<span class="sep">|</span><span class="action-btn">Share</span><span class="count">0</span></div></li>
      <li class="post">Curabitur laoreet, elit in tincidunt condimentum, massa tortor adipiscing nisl, non condimentum orci nunc quis diam. Curabitur sed arcu ut ipsum tempor molestie sed eget ipsum.
        <div class="post-meta">Posted by: <span class="user">username details</span><span class="sep">|</span>2 hrs ago<span class="sep">|</span><span class="action-btn">Share</span><span class="count">0</span></div></li>
      <li class="post">Vivamus tempor feugiat felis nec fringilla. Aenean condimentum nunc ut felis pellentesque in aliquet orci pharetra. Duis pharetra pharetra est vel bibendum.
        <div class="post-meta">Posted by: <span class="user">username details</span><span class="sep">|</span>2 hrs ago<span class="sep">|</span><span class="action-btn">Share</span><span class="count">0</span></div></li>
    </ul>
  </section>

  <footer class="footer-nav">
    <div class="footer-col" style="width:202px;--pad:34px"><h3>Home</h3><ul><li>Lorem ipsum dolor sit amet</li><li>Lorem ipsum dolor</li><li>Lorem ipsum dolor sit amet</li><li>Lorem ipsum</li></ul></div>
    <div class="footer-col" style="width:188px;--pad:22px"><h3>About</h3><ul><li>Lorem ipsum dolor sit amet</li><li>Lorem ipsum</li><li>Lorem ipsum dolor</li><li>Lorem ipsum dolor sit</li></ul></div>
    <div class="footer-col" style="width:197px;--pad:23px"><h3>Services</h3><ul><li>Lorem ipsum</li><li>Lorem ipsum dolor sit amet</li><li>Lorem ipsum dolor</li><li>Lorem ipsum</li></ul></div>
    <div class="footer-col" style="width:182px;--pad:21px"><h3>Faq</h3><ul><li>Lorem ipsum dolor sit</li><li>Lorem ipsum</li><li>Lorem ipsum dolor sit</li><li>Lorem ipsum dolor sit amet</li></ul></div>
    <div class="footer-col" style="width:206px;--pad:24px"><h3>Contact</h3><ul><li>Lorem ipsum dolor sit</li><li>Lorem ipsum dolor</li><li>Lorem ipsum dolor sit amet</li><li>Lorem ipsum</li></ul></div>
  </footer>
</div>
<p class="copyright">© 2011 Clearwell.&nbsp; All rights reserved</p>
</body>
</html>
```